BRAVO Property Concierge

We require a website built for this company. Logo is also on the attached document. Some info on the company:<br/>To create a work class experience for our clients for property maintenance. A personalised service that deliver’s what landlords need...Quality work, on time and managed from start to finish.<br/>We do things different, our clients deal with one contact, a client manager who manages your maintenance task from start to finish. Our service allows our expert trades people to do what they do best and leave the management/organising to us!<br/>I have drafted up the layout of the web ... very brief at this stage however once we have more info we will add links and can collate more information and provide. <br/>We just want to get a layout of what you think the web should look like and can go from there.

```html
<!DOCTYPE html>
<html lang="en">
<head>
<meta charset="utf-8">
<title>BRAVO Property Concierge</title>
<link href="https://fonts.googleapis.com/css2?family=Lato:wght@400;700;900&display=swap" rel="stylesheet">
<style>
:root{
  --yellow:#fdc300;
  --dark:#262626;
  --card:#3d3d3d;
  --footer:#2b2b2b;
  --light:#eeeced;
  --text:#2a2a2a;
  --white:#ffffff;
}
*{margin:0;padding:0;box-sizing:border-box}
html,body{width:1200px;height:3391px;overflow:hidden}
body{position:relative;background:var(--white);font-family:"Lato",sans-serif;color:var(--text)}
.abs{position:absolute}
.brand{position:absolute;display:flex;align-items:center;gap:12px;color:var(--white);font-weight:700;font-size:22px;line-height:26px}
.brand .mark{width:22px;height:22px;background:var(--yellow);flex:none}
.nav{position:absolute;top:70px;left:539px}
.nav a{color:var(--white);font-size:15px;font-weight:700;text-decoration:none;position:absolute;white-space:nowrap}
.hero-title{position:absolute;right:73px;top:262px;text-align:right;color:var(--white);font-weight:900}
.hero-title .big{font-size:88px;line-height:1}
.hero-title .small{font-size:36px;margin-top:8px}
.dot{position:absolute;width:18px;height:18px;border-radius:50%;background:var(--white);top:600px}
h2{font-size:27px;font-weight:900;color:var(--text)}
p.body{font-size:16px;line-height:28px}
.btn{position:absolute;background:var(--yellow);color:var(--white);font-weight:900;font-size:18px;border-radius:26px;width:198px;height:52px;display:flex;align-items:center;justify-content:center}
.services{position:absolute;left:75px;top:1365px;width:1051px;height:490px;background:var(--dark);border-radius:30px}
.services-under{position:absolute;left:75px;top:1350px;width:1051px;height:522px;background:var(--yellow);border-radius:32px;transform:rotate(-0.6deg)}
.svc{position:absolute;top:130px;width:304px;height:297px;background:var(--card);border-radius:28px;text-align:center;color:var(--white);padding-top:38px}
.svc h3{font-size:18px;font-weight:900;margin-top:22px}
.svc p{font-size:13.5px;line-height:25px;color:#d6d6d6;padding:6px 14px 0}
.more{color:var(--yellow);font-weight:900;font-size:14px;margin-top:14px;display:block}
.member-shadow{position:absolute;width:242px;height:305px;background:var(--yellow);border-radius:28px}
.member{position:absolute;width:242px;height:305px;background:var(--light);border-radius:28px;text-align:center;padding-top:112px}
.member h3{font-size:19px;font-weight:900}
.member p{font-size:14px;line-height:25px;color:#444;padding:8px 22px 0}
.avatar{position:absolute;width:146px;height:146px;border-radius:50%;border:4px solid var(--yellow);background:linear-gradient(180deg,#d9d6d2,#9a918a)}
.footer{position:absolute;left:0;top:3078px;width:1200px;height:313px;background:var(--footer);color:#cfcfcf}
.footer h4{font-size:16px;font-weight:700;color:var(--white);margin-bottom:13px}
.footer ul{list-style:none;font-size:14px;line-height:33px}
.social{position:absolute;top:249px;width:18px;height:18px;border-radius:50%;background:#9a9a9a}
</style>
</head>
<body>

<!-- Hero -->
<svg class="abs" style="left:0;top:0" width="1200" height="740" viewBox="0 0 1200 740">
  <defs>
    <linearGradient id="sky" x1="0" y1="0" x2="0" y2="1">
      <stop offset="0" stop-color="#4e6f9a"/>
      <stop offset="0.45" stop-color="#8fa3bc"/>
      <stop offset="0.7" stop-color="#c9c8c4"/>
      <stop offset="1" stop-color="#5a6b3a"/>
    </linearGradient>
  </defs>
  <path d="M0,55 L345,700 Q362,728 395,725 L1200,662 V682 L390,738 Q342,742 325,708 L0,100Z" style="fill:var(--yellow)"/>
  <path d="M0,0 H1200 V655 L400,712 Q365,716 350,690 L0,110Z" fill="url(#sky)" role="img" aria-label="Photo of a modern white apartment building under a blue sky"/>
</svg>
<div class="brand" style="left:74px;top:50px"><span class="mark"></span><span>BRAVO<br>Property Concierge</span></div>
<nav class="nav">
  <a style="left:0;color:var(--yellow)">HOME</a>
  <a style="left:101px">ABOUT US</a>
  <a style="left:233px">SERVICES</a>
  <a style="left:360px">BENEFITS</a>
  <a style="left:486px">CONTACT US</a>
</nav>
<div class="hero-title"><div class="big">BRAVO</div><div class="small">PROPERTY CONCIERGE</div></div>
<div class="dot" style="left:1037px"></div>
<div class="dot" style="left:1072px"></div>
<div class="dot" style="left:1106px;background:var(--yellow)"></div>

<!-- Welcome -->
<svg class="abs" style="left:0;top:780px" width="1200" height="790" viewBox="0 0 1200 790">
  <path d="M0,55 L790,3 Q835,0 858,38 L1200,640 V783 H0Z" style="fill:var(--light)"/>
  <path d="M0,55 L790,3 Q835,0 862,45 L872,62" fill="none" style="stroke:var(--yellow)" stroke-width="12"/>
  <path d="M1108,462 L1200,628" fill="none" style="stroke:var(--yellow)" stroke-width="16"/>
</svg>
<h2 class="abs" style="left:75px;top:928px">WELCOME TO OUR WEBSITE</h2>
<p class="body abs" style="left:74px;top:977px;width:520px">Etiam nisi orci, vehicula sit amet nunc sit amet, varius dapibus lectus. Integer et euismod lacus. Etiam justo diam, condimentum et aliquet id, laoreet vel orci. Etiam aliquam neque libero.<br>Donec at vulputate mauris. Nulla facilisi uisque vel ligula et lectus volutpat tempor.</p>
<div class="btn" style="left:75px;top:1141px">READ MORE</div>
<svg class="abs" style="left:620px;top:850px" width="507" height="393" viewBox="0 0 507 393">
  <defs><linearGradient id="meet" x1="0" y1="0" x2="1" y2="1"><stop offset="0" stop-color="#f2f2f2"/><stop offset="0.6" stop-color="#c8c3bd"/><stop offset="1" stop-color="#5c5a58"/></linearGradient></defs>
  <path d="M25,0 H477 Q507,0 507,30 V363 Q507,393 477,393 H90 Q60,393 55,363 L0,30 Q-3,0 25,0 Z" fill="url(#meet)" role="img" aria-label="Photo of a consultant shaking hands with a couple in a bright living room"/>
</svg>

<!-- Services -->
<div class="services-under"></div>
<div class="services">
  <h2 class="abs" style="left:0;width:100%;text-align:center;top:60px;color:var(--white)">OUR SERVICES</h2>
  <div class="svc" style="left:26px">
    <svg width="60" height="58" viewBox="0 0 60 58" fill="#fff"><circle cx="30" cy="14" r="10"/><circle cx="11" cy="18" r="7"/><circle cx="49" cy="18" r="7"/><path d="M14,56 Q14,28 30,28 Q46,28 46,56Z"/><path d="M0,48 Q0,28 11,28 Q18,28 20,33 Q12,40 12,48Z"/><path d="M60,48 Q60,28 49,28 Q42,28 40,33 Q48,40 48,48Z"/></svg>
    <h3>TRADE PEOPLE</h3>
    <p>Etiam nisi orci, vehicula sit amet nunc sit amet, varius dapibus lectus. Integer et euismod lacus.</p>
    <span class="more">READ MORE</span>
  </div>
  <div class="svc" style="left:373px">
    <svg width="60" height="58" viewBox="0 0 60 58" fill="none" stroke="#fff" stroke-width="4"><rect x="3" y="12" width="54" height="36" rx="3"/><circle cx="30" cy="30" r="11" fill="#fff"/><text x="30" y="36" font-size="16" font-weight="900" fill="#3d3d3d" stroke="none" text-anchor="middle" font-family="Lato,sans-serif">1</text></svg>
    <h3>FINANCE</h3>
    <p>Etiam nisi orci, vehicula sit amet nunc sit amet, varius dapibus lectus. Integer et euismod lacus.</p>
    <span class="more">READ MORE</span>
  </div>
  <div class="svc" style="left:719px">
    <svg width="60" height="58" viewBox="0 0 60 58" fill="#fff"><rect x="23" y="2" width="14" height="12"/><rect x="2" y="42" width="14" height="12"/><rect x="23" y="42" width="14" height="12"/><rect x="44" y="42" width="14" height="12"/><path d="M28,14h4v12h21v16h-4V30H32v12h-4V30H11v12H7V26h21z"/></svg>
    <h3>CONNECTIONS</h3>
    <p>Etiam nisi orci, vehicula sit amet nunc sit amet, varius dapibus lectus. Integer et euismod lacus.</p>
    <span class="more">READ MORE</span>
  </div>
</div>
<svg class="abs" style="left:43px;top:1596px" width="16" height="26" viewBox="0 0 16 26"><path d="M13,3 L4,13 L13,23" stroke="#262626" stroke-width="4" fill="none"/></svg>
<svg class="abs" style="left:1141px;top:1596px" width="16" height="26" viewBox="0 0 16 26"><path d="M3,3 L12,13 L3,23" stroke="#262626" stroke-width="4" fill="none"/></svg>

<!-- Team -->
<h2 class="abs" style="left:0;width:1200px;text-align:center;top:1932px">OUR TEAM</h2>
<p class="body abs" style="left:100px;width:1000px;text-align:center;top:1980px">Etiam nisi orci, vehicula sit amet nunc sit amet, varius dapibus lectus. Integer et euismod lacus. Etiam justo diam, condimentum et aliquet id, laoreet vel orciliquam neque libero.</p>

<div class="member-shadow" style="left:212px;top:2133px;transform:rotate(-1.5deg)"></div>
<div class="member" style="left:210px;top:2125px"><h3>NORA KEANE</h3><p>Etiam nisi orci, vehicula sit amet nunc sit amet, varius dapibus lectus. Integer et euismod lacus.</p><span class="more" style="margin-top:24px">READ MORE</span></div>
<div class="avatar" style="left:258px;top:2073px" role="img" aria-label="Portrait photo of a team member"></div>

<div class="member-shadow" style="left:482px;top:2133px;transform:rotate(-1.5deg)"></div>
<div class="member" style="left:480px;top:2125px"><h3>ELENA PARDO</h3><p>Etiam nisi orci, vehicula sit amet nunc sit amet, varius dapibus lectus. Integer et euismod lacus.</p><span class="more" style="margin-top:24px">READ MORE</span></div>
<div class="avatar" style="left:528px;top:2073px" role="img" aria-label="Portrait photo of a team member"></div>

<div class="member-shadow" style="left:752px;top:2133px;transform:rotate(-1.5deg)"></div>
<div class="member" style="left:750px;top:2125px;padding-top:116px"><h3>DANIEL GROVE</h3><p>Etiam nisi orci, vehicula sit amet nunc sit amet, varius dapibus lectus. Integer et euismod lacus.</p><span class="more" style="margin-top:20px">READ MORE</span></div>
<div class="avatar" style="left:798px;top:2073px" role="img" aria-label="Portrait photo of a team member"></div>

<!-- Benefit -->
<svg class="abs" style="left:0;top:2540px" width="1200" height="540" viewBox="0 0 1200 540">
  <path d="M0,540 V85 L330,85 Q362,5 425,5 L1200,58 V540Z" style="fill:var(--light)"/>
  <path d="M320,92 Q358,5 425,5 L1200,58" fill="none" style="stroke:var(--yellow)" stroke-width="12"/>
  <path d="M35,540 L70,480 H95 L60,540Z" style="fill:var(--yellow)"/>
</svg>
<svg class="abs" style="left:75px;top:2628px" width="506" height="393" viewBox="0 0 506 393">
  <defs><linearGradient id="worker" x1="0" y1="0" x2="1" y2="1"><stop offset="0" stop-color="#8a6a52"/><stop offset="0.45" stop-color="#d9c44a"/><stop offset="0.75" stop-color="#3b4a6b"/><stop offset="1" stop-color="#c8b8a5"/></linearGradient></defs>
  <path d="M30,0 H476 Q506,0 503,30 L455,363 Q450,393 420,393 H30 Q0,393 0,363 V30 Q0,0 30,0Z" fill="url(#worker)" role="img" aria-label="Photo of a tradesman in a hard hat and hi-vis vest writing on a clipboard"/>
</svg>
<h2 class="abs" style="left:614px;top:2692px">BENEFIT</h2>
<p class="body abs" style="left:614px;top:2741px;width:520px">Etiam nisi orci, vehicula sit amet nunc sit amet, varius dapibus lectus. Integer et euismod lacus. Etiam justo diam, condimentum et aliquet id, laoreet vel orci. Etiam aliquam neque libero.<br>Donec at vulputate mauris. Nulla facilisi uisque vel ligula et lectus volutpat tempor.</p>
<div class="btn" style="left:614px;top:2905px">READ MORE</div>

<!-- Footer -->
<footer class="footer">
  <div class="brand" style="left:74px;top:100px"><span class="mark"></span><span>BRAVO<br>Property Concierge</span></div>
  <p class="abs" style="left:75px;top:170px;font-size:13px;line-height:24px">Copyright © 2019 Company Name.<br>All Right Reserved</p>
  <span class="social" style="left:73px"></span>
  <span class="social" style="left:108px"></span>
  <span class="social" style="left:147px"></span>
  <span class="social" style="left:190px"></span>
  <span class="social" style="left:230px"></span>
  <div class="abs" style="left:350px;top:60px"><h4>SITE MAP</h4><ul><li>About us</li><li>Services</li><li>Benefits</li><li>Contact Us</li></ul></div>
  <div class="abs" style="left:580px;top:60px"><h4>SERVICES</h4><ul><li>Trade people</li><li>Removalist van and trailers</li><li>Connections</li><li>Smoke alarms</li><li>Finance</li><li>Wealth creation</li></ul></div>
  <div class="abs" style="left:891px;top:60px"><h4>BENEFIT</h4><ul><li>Customer service</li><li>Call centre</li><li>Values</li><li>Pricing</li><li>Level of expertise</li></ul></div>
</footer>

</body>
</html>
```